Visitenkarten-Design für Ferienhausvermietung
Zielgruppe
Vermietung eines Ferienhauses
Aufgabenstellung
Die Visitenkarte sollte edel und hochwertig wirken...
Es wäre mir wichtig, dass die Visitenkarte im Querformat erstellt wird.
Die Farben vom Logo lauten:
green: C = 43 M = 0 Y = 100 N = 16
brown: C = 39 M = 57 J = 87 N = 53
sky blue: C = 14 M = 6 J = 6 N = 0
Aber bitte nicht so viel in den Visitenkarten verwenden. Die Visitenkarten sollen eher neutral gehalten werden.
Die Schriften
font
Lindeneck : Satisfaction
Ferienhaus : Corbert Regular
Flyer-Design für Ferienhausvermietung Flyer-Design für Ferienhausvermietung"
Es soll ein Flyer im Format DIN A4 erstellt werden. Der beidseitig bedruckt wird und dann 6seitig gefaltet wird. Ich benötige für den Flyer: Beschreibung/Ausstattung des Ferienhauses Beschreibung der Lage Beschreibung der Umgebung Anfahrt/Lage/Kontakt
Logo-Design für Ferienhaus ´Sa Morta´auf Mallorca mit eigenem Tennisplatz und Pool Logo-Design für Ferienhaus ´Sa Morta´auf Mallorca mit eigenem Tennisplatz und Pool"
Sie können sich meine Finca auf der Website: Casitorvent anschauen. Ort: Costitx Name des Hauses: Finca Reblat (heißt nur auf der Website so). Der Name am Tor Haus: Finca Sa Morta. Ich mag es gerne klassisch
Logo-Design für ein Feriendorf an der Ostsee Logo-Design für ein Feriendorf an der Ostsee"
* Nicht zu bunt, nicht zu verspielt, möglichst klar und aufgeräumt * In 2D, keine Schattierungen, keine Fotos im Hintergrund o. ä.. * Das Logo muss in allen Medien gut darstellbar sein! * Es sollte modern wirken, dennoch fröhlich, warm und einladend * Der Strand-/Wasserbezug muss deutlich we..
Flyer-Design für Ferienhaus Flyer-Design für Ferienhaus"
Flyerdesign für Ferienhaus: Din-Lang 2x gefalzt (übliche Format), 3 Seiten vorne und hinten.  Es sollte nach Möglichkeit an unsere Webseite (www.ferienhaus-kormoran-tidewik.de) angepasst werden, druckfertig sein und per PDF auf unserer Webseite zum Downloaden integriert werden können. Meh..
Logo-Design für Ferienhaus Logo-Design für Ferienhaus"
Wir suchen ein Moderenes Design gern berücksichtig in Kombination mit dem Naturpark Velmtaler Höhen. Da das Ferienhaus sich dort befindet.

```html
<!DOCTYPE html>
<html lang="de">
<head>
<meta charset="utf-8">
<title>Ferienhaus Lindeneck – Visitenkarte</title>
<link rel="stylesheet" href="https://fonts.googleapis.com/css2?family=Saira:wght@400&family=Mrs+Saint+Delafield&display=swap">
<style>
  :root {
    --paper: #ffffff;
    --ink-brown: #2c1b14;
    --logo-green: #6fd21c;
    --house-tint: #e6ddd3;
    --leaf-tint: #e4f0d6;
  }
  html, body {
    margin: 0;
    padding: 0;
    width: 1200px;
    height: 786px;
    overflow: hidden;
    background: var(--paper);
  }
  .card {
    position: relative;
    width: 1200px;
    height: 786px;
    background: var(--paper);
    overflow: hidden;
    font-family: "Saira", "Segoe UI", sans-serif;
    color: var(--ink-brown);
  }
  .backdrop-art {
    position: absolute;
    left: 0;
    top: 300px;
    width: 1200px;
    height: 486px;
  }
  .brand-mark {
    position: absolute;
    left: 68px;
    top: 58px;
    width: 268px;
    height: 268px;
    border: 3px solid var(--ink-brown);
    border-radius: 50%;
    box-sizing: border-box;
    display: flex;
    align-items: center;
    justify-content: center;
  }
  .brand-mark__name {
    font-size: 40px;
    font-weight: 400;
    color: var(--ink-brown);
    letter-spacing: 0.5px;
  }
  .house-title {
    position: absolute;
    left: 548px;
    top: 112px;
    margin: 0;
    font-size: 50px;
    font-weight: 400;
    color: var(--logo-green);
    letter-spacing: 0.3px;
    line-height: 1;
  }
  .host-name {
    position: absolute;
    left: 330px;
    top: 322px;
    margin: 0;
    font-family: "Mrs Saint Delafield", cursive;
    font-size: 150px;
    font-weight: 400;
    line-height: 1;
    color: var(--ink-brown);
    text-shadow: 2px 5px 6px rgba(44, 27, 20, 0.35);
    white-space: nowrap;
  }
  .contact {
    position: absolute;
    top: 604px;
    margin: 0;
    font-size: 34px;
    line-height: 43px;
    font-style: normal;
    color: var(--ink-brown);
    white-space: nowrap;
  }
  .contact--postal { left: 105px; }
  .contact--online {
    right: 111px;
    top: 647px;
    text-align: right;
  }
</style>
</head>
<body>
  <main class="card">
    <svg class="backdrop-art" role="img" aria-label="Faint drawing of the holiday house framed by leafy trees" viewBox="0 0 1200 486">
      <defs>
        <radialGradient id="house-glow" cx="0.5" cy="0.5" r="0.5">
          <stop offset="0" stop-color="#e6ddd3" stop-opacity="0.7"/>
          <stop offset="1" stop-color="#e6ddd3" stop-opacity="0"/>
        </radialGradient>
        <radialGradient id="leaf-glow" cx="0.5" cy="0.5" r="0.5">
          <stop offset="0" stop-color="#e4f0d6" stop-opacity="0.95"/>
          <stop offset="1" stop-color="#e4f0d6" stop-opacity="0"/>
        </radialGradient>
      </defs>
      <ellipse cx="680" cy="360" rx="480" ry="260" fill="url(#house-glow)"/>
      <ellipse cx="60" cy="260" rx="220" ry="280" fill="url(#leaf-glow)"/>
      <ellipse cx="1140" cy="180" rx="220" ry="300" fill="url(#leaf-glow)"/>
    </svg>

    <div class="brand-mark">
      <span class="brand-mark__name">Lindeneck</span>
    </div>

    <h1 class="house-title">Ferienhaus Lindeneck</h1>

    <p class="host-name">Marlene Hofbauer</p>

    <address class="contact contact--postal">
      Lindenweg 12<br>
      91742 Ahornfeld<br>
      Tel: 01234/4718256
    </address>

    <address class="contact contact--online">
      info@lindeneck-ferienhaus.de<br>
      www.lindeneck-ferienhaus.de
    </address>
  </main>
</body>
</html>
```